Oversized( 8.52 by 4.57) handout postcards.
We need promotional post cards that our congregation can use to pass out to their frineds and family for a special Easter Week Awakening. I attempted to create "something" but was not completely satisfied with it. I have included my attempt in the uploaded images.
Trhe front part of the post card I would like for it to capture the attention of people. The Backside of the postcard can contain event information.
About the Event Information.
Easter Week Awakening
Special Guest: Dale Wickersham (www.dalewickersham-example.com)
Dates: Sunday March 15 thru Wednesday March 18
Times: Sunday 9:00 a.m., 11:00 a.m., and 6:00 p.m.
Monday - Wednesday 6:00 p.m. with a free meal being served at 5:00 p.m.
Our Location is 418 N. Marlow Street, Independence, KS 67399
Our Phone Number 620-555-0147

```html
<!DOCTYPE html>
<html lang="en">
<head>
<meta charset="utf-8">
<title>Easter Week Awakening Postcard</title>
<link href="https://fonts.googleapis.com/css2?family=Cinzel:wght@400;600;700&display=swap" rel="stylesheet">
<style>
  :root {
    --navy: #1d3f7a;
    --deep: #0a2347;
    --sky: #b9d0e6;
    --panel: #0e2336;
    --accent: #e2691f;
    --ink: #222;
    --white: #ffffff;
    --faint: #6f8fae;
  }
  * { margin: 0; padding: 0; box-sizing: border-box; }
  html, body { width: 1200px; height: 1000px; overflow: hidden; background: var(--white); }
  body { position: relative; font-family: "Cinzel", serif; color: var(--ink); }

  .sheet-label {
    position: absolute; left: 936px; top: 58px;
    font-size: 26px; line-height: 34px; color: var(--navy);
  }

  .card {
    position: absolute; left: 328px; width: 570px; height: 442px;
    background: var(--white); overflow: hidden;
    box-shadow: 4px 6px 14px rgba(0,0,0,0.35);
  }
  .card--front { top: 56px; background: linear-gradient(180deg, #ffffff 0%, #ffffff 35%, var(--sky) 80%); }
  .card--back { top: 524px; }

  .layer { position: absolute; }

  /* front */
  .paint-edge {
    left: 0; top: 0; width: 570px; height: 60px;
    background: linear-gradient(180deg, rgba(30,110,170,0.85) 0%, rgba(70,140,190,0.35) 55%, rgba(255,255,255,0) 100%);
  }
  .ministry-name {
    left: 20px; top: 24px; display: flex; align-items: center; gap: 6px;
    font-size: 13px; font-weight: 600; color: var(--ink);
  }
  .ministry-name .dot { width: 12px; height: 12px; border-radius: 50%; background: var(--ink); }
  .speaker-photo {
    left: 100px; top: 44px; width: 236px; height: 300px;
    background: radial-gradient(ellipse at 55% 45%, #d9cbb6 0%, #b8a68c 45%, #8d98a5 80%, rgba(141,152,165,0) 100%);
  }
  .story {
    left: 347px; top: 80px; width: 215px;
    font-size: 13.5px; line-height: 24.5px; color: var(--navy);
  }
  .story .until { margin-top: 10px; }
  .band { left: 0; top: 0; width: 570px; height: 442px; }
  .church-mark {
    left: 440px; top: 272px; width: 112px; text-align: center;
    font-size: 13px; line-height: 19px; color: var(--white);
  }
  .church-mark-bg {
    left: 436px; top: 262px; width: 120px; height: 90px; background: #2a5a96;
  }
  .title { left: 46px; top: 326px; color: var(--white); }
  .title .kicker { font-size: 18px; letter-spacing: 0.5px; }
  .title .main { font-size: 40px; font-weight: 700; line-height: 44px; letter-spacing: 1px; }
  .featuring { left: 46px; top: 398px; color: var(--white); display: flex; align-items: baseline; gap: 14px; }
  .featuring .label { font-size: 11px; }
  .featuring .name { font-size: 17px; font-style: italic; }
  .dates { right: 14px; top: 398px; color: var(--white); font-size: 17px; }
  .dates sup { font-size: 9px; }

  /* back */
  .info-panel { left: 0; top: 0; width: 275px; height: 442px; background: var(--panel); }
  .panel-photo {
    left: 0; top: 0; width: 275px; height: 442px;
    background: radial-gradient(ellipse at 15% 50%, rgba(48,110,150,0.75) 0%, rgba(22,60,90,0.5) 45%, rgba(14,35,54,0) 80%);
  }
  .back-head { left: 12px; top: 58px; width: 255px; display: flex; align-items: center; gap: 8px; color: var(--white); }
  .back-head .church { font-size: 9.5px; line-height: 12px; text-align: center; flex: none; }
  .back-head .kicker { font-size: 12px; }
  .back-head .main { font-size: 23px; font-weight: 700; line-height: 26px; }
  .details {
    left: 0; top: 152px; width: 275px; text-align: center;
    color: var(--white); font-size: 10px; line-height: 16px;
  }
  .details sup { font-size: 6px; }
  .details .accent { color: var(--accent); }
  .details .guest-name { font-size: 17px; font-style: italic; line-height: 22px; }
  .details .gap { height: 8px; }
  .back-footer {
    left: 14px; top: 402px; width: 250px; display: flex; justify-content: space-between; align-items: center;
    color: var(--faint); font-size: 11px;
  }
  .back-footer .item { display: flex; align-items: center; gap: 5px; }
  .back-footer .sq { width: 10px; height: 10px; background: var(--faint); }
  .stamp-box { left: 447px; top: 23px; width: 95px; height: 112px; border: 1px solid #222; }
  .address-line { left: 329px; width: 199px; height: 0; border-top: 1.5px solid #222; }
</style>
</head>
<body>
  <div class="sheet-label">Postcard<br>Design</div>

  <section class="card card--front">
    <div class="layer paint-edge" role="img" aria-label="Blue paint splatter border"></div>
    <div class="layer ministry-name"><span class="dot"></span>dalewickersham ministries</div>
    <div class="layer speaker-photo" role="img" aria-label="Photo of the guest speaker seated in prayer on a stone ledge"></div>
    <div class="layer story">
      <p>He had nine step-fathers,<br>an alcoholic mother,<br>was abused &amp; neglected,<br>left without hope.</p>
      <p class="until">Until ....</p>
    </div>
    <svg class="layer band" viewBox="0 0 570 442" aria-hidden="true">
      <defs>
        <linearGradient id="bandFill" x1="0" y1="0" x2="0" y2="1">
          <stop offset="0" stop-color="#2a7cc4"/>
          <stop offset="1" stop-color="#071c3d"/>
        </linearGradient>
      </defs>
      <polygon points="0,318 140,282 430,346 570,322 570,442 0,442" fill="url(#bandFill)"/>
      <polyline points="0,318 140,282 430,346 570,322" fill="none" stroke="#5fa6dd" stroke-width="3"/>
    </svg>
    <div class="layer church-mark-bg"></div>
    <div class="layer church-mark">Cornerstone<br>Chapel<br>Independence</div>
    <div class="layer title">
      <div class="kicker">Easter Week</div>
      <div class="main">AWAKENING</div>
    </div>
    <div class="layer featuring"><span class="label">Featuring</span><span class="name">Dale Wickersham</span></div>
    <div class="layer dates">On March 15<sup>th</sup> – 18<sup>th</sup></div>
  </section>

  <section class="card card--back">
    <div class="layer info-panel"></div>
    <div class="layer panel-photo" role="img" aria-label="Faded blue-toned portrait of the guest speaker"></div>
    <div class="layer back-head">
      <div class="church">Cornerstone<br>Chapel<br>Independence</div>
      <div>
        <div class="kicker">Easter Week</div>
        <div class="main">AWAKENING</div>
      </div>
    </div>
    <div class="layer details">
      <p class="accent">Special Guest:</p>
      <p class="accent">Featuring</p>
      <p class="accent guest-name">Dale Wickersham</p>
      <div class="gap"></div>
      <p>On</p>
      <p>Sunday, March 15<sup>th</sup> thru</p>
      <p>Wednesday March 18<sup>th</sup></p>
      <div class="gap"></div>
      <p>Sunday 9:00 a.m., 11:00 a.m., and 6:00 p.m.</p>
      <p>Monday - Wednesday 6:00 p.m.</p>
      <p>with a free meal being served at 5:00 p.m.</p>
      <div class="gap"></div>
      <p>At</p>
      <p>418 N. Marlow Street, Independence, KS 67399</p>
    </div>
    <div class="layer back-footer">
      <span class="item"><span class="sq"></span>Cornerstone Chapel</span>
      <span class="item">dalewickersham</span>
    </div>
    <div class="layer stamp-box"></div>
    <div class="layer address-line" style="top:247px"></div>
    <div class="layer address-line" style="top:278px"></div>
    <div class="layer address-line" style="top:309px"></div>
    <div class="layer address-line" style="top:339px"></div>
  </section>
</body>
</html>
```